1 page A4 double sided Brochure Design Folded to envelope size. Interesting fold design would be co

Small family run guesthouse BnB in Blue Mountains Australia needs a new brochure showing different aspects of business

We need a new brochure to go with our new website. Basically the design would be good as a double sided brochure that can be folded down to standard envelope size.

We have seen a few interesting brochure designs before that fold in different ways (and therefore have the design to match) but still fold down to this size to help with postage.

The design would have to showcase the different aspects of our business including individual accommodation for couples and families, conference market, wedding market, retreat market and events market (parties, re-unions etc). The Business must be Showcased as The Fernlight Lodge, Blue Mountains

It is possible to arrange design so folds separate different sections of info/pictures.

It is also optional that we possibly have 2 brochures instead, one that is a basic all inclusive once described and one that only deals with group bookings (wedding conference retreats etc etc)

Must match design elements from our web page. Feel free to take informations, elements and images from there for design www.fernlightlodge-example.com.au

Here is a link to our view we wake up to every morning to inspire all those working on a design!
http://www.fernlightlodge-example.com.au/images/view.jpg

Target Market(s)

Group bookings, weddings, conferences, retreats, events and Blue Mountains Travellers

Industry/Entity Type

Accommodation

Requirements
Must have
• Must be based on our current websites design feel, colours, etc
Must be showcased as The Fernlight Lodge Blue Mountains.
Must mention The Blue Mountains as a world heritage destination
Must be A4 double sided that can fold down to 1/3 the size to fit into a standard envelope. Any designs that will not fit in a standard envelope once folded can not be accepted as they are outside the brief
Nice to have
• Interesting folding design to get people interested to read it.

```html
<!DOCTYPE html>
<html lang="en">
<head>
<meta charset="utf-8">
<title>The Fernlight Lodge, Blue Mountains – Brochure</title>
<link rel="stylesheet" href="https://fonts.googleapis.com/css2?family=Lato:wght@300;400&display=swap">
<style>
  :root {
    --sage-mist: #eef0e9;
    --sage-deep: #dfe3d8;
    --bark: #3b312c;
    --bark-soft: #5a4d45;
    --leaf-panel: #e5eed6;
    --paper: #ffffff;
    --ink: #4a423d;
    --heading-ink: #3e3632;
  }
  * { box-sizing: border-box; margin: 0; padding: 0; }
  html, body { width: 1200px; height: 850px; overflow: hidden; background: var(--paper); }
  .brochure {
    position: relative; width: 1200px; height: 850px; overflow: hidden;
    font-family: "Lato", "Helvetica Neue", Arial, sans-serif; color: var(--ink);
    background: var(--paper);
  }
  .hero {
    position: absolute; left: 0; top: 0; width: 1200px; height: 300px;
    background: linear-gradient(90deg, #e4e7df 0%, var(--sage-mist) 45%, #f4f5f1 100%);
  }
  .hero-tagline {
    position: absolute; left: 100px; top: 58px; width: 420px;
    text-align: center; font-weight: 300; color: var(--heading-ink);
  }
  .hero-tagline .lead { font-size: 19.5px; line-height: 25px; }
  .hero-tagline .emphasis { font-size: 31px; line-height: 38px; margin-top: 4px; }
  .hero-trees {
    position: absolute; left: 530px; top: 30px; width: 640px; height: 265px;
    background: radial-gradient(ellipse at 65% 40%, #b9aea4 0%, #d8d6cd 55%, rgba(238,240,233,0) 75%);
  }
  .band { position: absolute; left: 0; top: 280px; width: 1200px; height: 220px; }
  .photo-strip { position: absolute; top: 316px; height: 158px; }
  .photo-dining { left: 0; width: 290px; background: linear-gradient(135deg, #a98f52, #d9c79a 55%, #8a7444); }
  .photo-room { left: 294px; width: 301px; background: linear-gradient(135deg, #6d8a6a, #e7e3d8 55%, #b04a32); }
  .photo-valley { left: 600px; width: 328px; background: radial-gradient(circle at 70% 35%, #dfe8f4 0%, #6a8fc4 30%, #2b3320 80%); }
  .photo-pool { left: 932px; width: 268px; background: linear-gradient(180deg, #b47a5a 0%, #9b5c41 55%, #3d8fb5 75%, #6fb7d6 100%); }
  .lodge-panel {
    position: absolute; left: 0; top: 498px; width: 600px; height: 352px;
    background: var(--leaf-panel);
  }
  .body-copy { font-size: 11.6px; line-height: 14.6px; font-weight: 400; color: var(--ink); }
  .body-copy p + p { margin-top: 14px; }
  .col { position: absolute; top: 530px; }
  .col-one { left: 38px; width: 252px; }
  .col-two { left: 318px; width: 262px; }
  .sister-photo { position: absolute; left: 626px; width: 265px; }
  .sister-lounge { top: 524px; height: 134px; background: linear-gradient(135deg, #caa84a, #e3c65b 50%, #7a3a2a); }
  .sister-bedroom { top: 670px; height: 170px; background: linear-gradient(135deg, #d9b43c, #f1dc7a 50%, #6c3a2c); }
  .sister-copy { position: absolute; left: 906px; top: 528px; width: 272px; }
  .sister-title { font-size: 11.6px; letter-spacing: 0.4px; margin-bottom: 14px; font-weight: 400; }
</style>
</head>
<body>
<main class="brochure">
  <section class="hero" role="img" aria-label="Faint photograph of the guesthouse building in soft sage tones"></section>
  <div class="hero-trees" role="img" aria-label="Ornamental illustration of two stylised gum trees"></div>
  <div class="hero-tagline">
    <p class="lead">Family owned and run Blue Mountains accomodation, retreat, conference, wedding and function centre set on</p>
    <p class="emphasis">32 acres of virgin bushland in the beauty of a world heritage location.</p>
  </div>

  <svg class="band" viewBox="0 0 1200 220" aria-hidden="true">
    <path fill="#3b312c" d="M0 12 H700 C760 12 790 -10 840 8 C870 18 900 2 940 6 C990 10 1010 -14 1060 4 C1100 16 1150 6 1200 10 V220 H0 Z"/>
  </svg>

  <div class="photo-strip photo-dining" role="img" aria-label="Photo of the sunlit dining room with round tables"></div>
  <div class="photo-strip photo-room" role="img" aria-label="Photo of a guest bedroom with garden doors"></div>
  <div class="photo-strip photo-valley" role="img" aria-label="Photo of morning mist over the valley"></div>
  <div class="photo-strip photo-pool" role="img" aria-label="Photo of the brick manor and swimming pool"></div>

  <section class="lodge-panel"></section>
  <div class="col col-one body-copy">
    <p>The Fernlight Lodge Blue Mountains is a small family run guesthouse, bush retreat and function centre.</p>
    <p>Located on 32 acres of pristine virgin bushland in the centre of world heritage listed national park land The Fernlight Lodge is your perfect Blue Mountains accommodation whether you are looking for a quiet place to escape with someone special or a function or conference venue in the Blue Mountains for your next group escape or private, personal, specially tailored wedding.</p>
    <p>The Fernlight Lodge has 2 buildings. The main retreat with 20 well appointed en suited rooms, each with views across the pool and valley, along with 2 function rooms, games</p>
  </div>
  <div class="col col-two body-copy">
    <p>room, commercial kitchen, pool and outdoor BBQ area.</p>
    <p>The second is our manor house, a large, simple 7 bedroom, 4 bathroom house with lounge kitchen and dining room.</p>
    <p>Together with our private, friendly, family run atmosphere The Fernlight Lodge is the perfect place to escape the real world and explore another.</p>
    <p>So close by... but worlds away</p>
    <p>Ridgeview Cottage is our smaller sister property in Katoomba perfect for families and small groups</p>
  </div>

  <div class="sister-photo sister-lounge" role="img" aria-label="Photo of the cottage lounge and dining table"></div>
  <div class="sister-photo sister-bedroom" role="img" aria-label="Photo of a cottage bedroom with yellow walls"></div>
  <div class="sister-copy body-copy">
    <h2 class="sister-title">RIDGEVIEW COTTAGE</h2>
    <p>Ridgeview Cottage is our smaller sister property located in Katoomba.</p>
    <p>It is the perfect Blue Mountains Accommodation for families and groups travelling together with a range of upmarket touches and accommodating up to 10 people.</p>
    <p>With 4 bedrooms, 2 bathrooms, full kitchen and spa Ridgeview Cottage is a perfect private place to based your small group for a Blue Mountains escape.</p>
    <p>You can check out Ridgeview Cottage at its own website at www.ridgeviewcottage-example.com.au</p>
  </div>
</main>
</body>
</html>
```